Responsive OnePage Design for recruitment company

BrightCrew is a modern company that sources interim people for its customers. Mostly developers, scrum master, project managers and designers. In this website we want to tell something about us, about how we work, our customers and we want our candidates be able to subscribe. The subscription form should be several fields (name, surname, email address, phone number and the possibility to upload your resume.We want it to fit into a existing wordpress plugin. We also want a listing of our job opportunities. The listing should be designed in a clear readable overview and if you click on the job you should get the details and be able to respond quickly by filling in you name, surname, email address, rate, phone number and upload your resume. We want this to be a standard configurable plugin. It should be easy to fill in the jobs in Wordpress by our administrator. We want a fresh, modern and cool design. It should be a responsive onepage design. If you click on a listed job you should stay on the same page. Our logo is added.

Target Market(s)

recruitment

Industry/Entity Type

Recruitment

Font styles to use
Sans Serif

Colors

Designer to choose colors to be used in the design.

Requirements
Must have
• Onepage design
• listing of job opportunities
• subscription forms
• be responsive

```html
<!DOCTYPE html>
<html lang="en">
<head>
<meta charset="utf-8">
<title>BrightCrew — Interim People</title>
<link rel="stylesheet" href="https://fonts.googleapis.com/css2?family=Montserrat:wght@500&family=Old+Standard+TT:wght@400;700&family=Open+Sans:wght@400;600;700&display=swap">
<style>
  :root {
    --stage: #4a4a4a;
    --page: #ffffff;
    --ink: #333333;
    --muted: #9a9a9a;
    --brand: #1e7fc4;
    --hero-deep: #17324d;
    --hero-mid: #2c5578;
    --dark-band: #141414;
    --dark-mid: #262626;
    --white: #ffffff;
    --line-soft: rgba(255,255,255,.75);
  }
  * { box-sizing: border-box; margin: 0; padding: 0; }
  html, body { width: 1200px; height: 1200px; overflow: hidden; background: var(--stage); }
  .page {
    position: absolute; left: 196px; top: 0; width: 814px; height: 1200px;
    background: var(--page); overflow: hidden;
    font-family: "Open Sans", Arial, sans-serif;
  }

  /* Header */
  .site-header { position: absolute; left: 0; top: 0; width: 100%; height: 42px; background: var(--page); }
  .brand {
    position: absolute; left: 110px; top: 11px;
    font-family: "Montserrat", sans-serif; font-weight: 500; font-size: 16px;
    letter-spacing: 3.6px; color: var(--brand);
  }
  .nav-item {
    position: absolute; top: 17px; transform: translateX(-50%);
    font-size: 7px; font-weight: 600; color: var(--ink); white-space: nowrap; letter-spacing: .2px;
  }
  .nav-item.is-active { color: var(--brand); }
  .nav-item.is-active::after {
    content: ""; position: absolute; left: 0; right: 0; bottom: -3px; height: 1px; background: var(--brand);
  }

  /* Hero */
  .hero { position: absolute; left: 0; top: 42px; width: 100%; height: 343px; }
  .hero-photo {
    position: absolute; inset: 0;
    background: linear-gradient(180deg, var(--hero-mid) 0%, var(--hero-deep) 100%);
  }
  .hero-welcome {
    position: absolute; top: 74px; width: 100%; text-align: center;
    font-family: "Old Standard TT", serif; font-weight: 700; font-size: 12px; color: var(--white);
  }
  .hero-title {
    position: absolute; top: 104px; width: 100%; text-align: center;
    font-family: "Old Standard TT", serif; font-weight: 700; font-size: 30px; line-height: 37px;
    color: var(--white); letter-spacing: 1px; transform: scaleX(.88);
  }
  .hero-roles {
    position: absolute; top: 193px; width: 100%; text-align: center;
    font-size: 10.5px; color: var(--white); letter-spacing: .3px;
  }
  .hero-arrow { position: absolute; top: 154px; }
  .hero-arrow.prev { left: 26px; }
  .hero-arrow.next { left: 743px; }
  .hero-dots { position: absolute; top: 315px; left: 373px; }

  /* Shared section heading */
  .section-title {
    position: absolute; left: 0; width: 100%; top: 42px; text-align: center;
    font-family: "Old Standard TT", serif; font-weight: 700; font-size: 24px; color: var(--ink); letter-spacing: .5px;
  }
  .title-rule { position: absolute; left: 393px; width: 29px; height: 4px; border-top: 1px solid #bbb; border-bottom: 1px solid #bbb; }

  /* About */
  .about { position: absolute; left: 0; top: 385px; width: 100%; height: 343px; text-align: center; }
  .about .title-rule { top: 74px; }
  .about-copy { position: absolute; left: 104px; width: 606px; font-size: 9.4px; line-height: 15.2px; color: var(--muted); }
  .about-copy.p1 { top: 88px; }
  .about-copy.p2 { top: 133px; }
  .about-copy.p3 { top: 209px; }

  /* How we work */
  .process { position: absolute; left: 0; top: 728px; width: 100%; height: 462px; }
  .process-photo {
    position: absolute; inset: 0;
    background: radial-gradient(ellipse at 50% 45%, var(--dark-mid) 0%, var(--dark-band) 75%);
  }
  .process .section-title { top: 46px; color: var(--white); font-size: 23px; }
  .process .title-rule { top: 78px; border-color: var(--line-soft); }
  .process-intro { position: absolute; top: 91px; width: 100%; text-align: center; font-size: 10.2px; color: #8a8a8a; }
  .process-map { position: absolute; left: 0; top: 0; }
  .step-label { font-family: "Open Sans", sans-serif; font-weight: 700; font-size: 9px; fill: var(--white); letter-spacing: .4px; word-spacing: 2px; }
  .map-brand { font-family: "Montserrat", sans-serif; font-weight: 500; font-size: 15px; letter-spacing: 3.5px; fill: var(--brand); }
</style>
</head>
<body>
<div class="page">

  <header class="site-header">
    <div class="brand">BRIGHTCREW</div>
    <nav>
      <span class="nav-item is-active" style="left:361px">HOME</span>
      <span class="nav-item" style="left:409px">ABOUT</span>
      <span class="nav-item" style="left:472px">HOW WE WORK</span>
      <span class="nav-item" style="left:552px">OUR CUSTOMERS</span>
      <span class="nav-item" style="left:626px">SUBSCRIBE</span>
      <span class="nav-item" style="left:690px">OUR JOB</span>
    </nav>
  </header>

  <section class="hero">
    <div class="hero-photo" role="img" aria-label="Team photo of the recruitment staff in business suits, tinted blue"></div>
    <p class="hero-welcome">Welcome to BrightCrew</p>
    <h1 class="hero-title">BRIGHTCREW IS A MODERN COMPANY<br>THAT SOURCES INTERIM PEOPLE</h1>
    <p class="hero-roles">DEVELOPERS - SCRUM MASTER - PROJECT MANAGERS - DESIGNERS</p>
    <svg class="hero-arrow prev" width="46" height="46" viewBox="0 0 46 46">
      <rect x="9" y="9" width="28" height="28" transform="rotate(45 23 23)" fill="none" stroke="rgba(255,255,255,.5)" stroke-width="1"/>
      <path d="M29 23H17M21 19l-4 4 4 4" fill="none" stroke="#fff" stroke-width="1.2"/>
    </svg>
    <svg class="hero-arrow next" width="46" height="46" viewBox="0 0 46 46">
      <rect x="9" y="9" width="28" height="28" transform="rotate(45 23 23)" fill="none" stroke="rgba(255,255,255,.5)" stroke-width="1"/>
      <path d="M17 23h12M25 19l4 4-4 4" fill="none" stroke="#1e7fc4" stroke-width="1.2"/>
    </svg>
    <svg class="hero-dots" width="70" height="4" viewBox="0 0 70 4">
      <rect x="0" y="1" width="20" height="1.5" fill="#fff"/>
      <rect x="25" y="1" width="20" height="1.5" fill="#fff"/>
      <rect x="50" y="1" width="20" height="1.5" fill="#1e7fc4"/>
    </svg>
  </section>

  <section class="about">
    <h2 class="section-title">ABOUT US</h2>
    <div class="title-rule"></div>
    <p class="about-copy p1">Lorem Ipsum is simply has been the industry's standard dummy text everdummy texto the printing and typesetting industry<br>. Lorem Ipsum has been the industry's standard dummy text ever since the 1500s.</p>
    <p class="about-copy p2">Lorem ipsum dolor sit amet, consectetur adipiscing elit, sed do eiusmod tempor incididunt ut labore et dolore magna aliqua. Ut enim ad minim veniam, quis nostrud exercitation ullamco laboris nisi ut aliquip ex ea commodo consequat. Duis aute irure dolor in reprehenderit in voluptate velit esse cillum dolore eu fugiat nulla pariatur. Excepteur sint occaecat cupidatat non proident, sunt in culpa qui officia deserunt mollit anim id est laborum.</p>
    <p class="about-copy p3">“Lorem Ipsum doesn’t exist because people think the content is meaningless window dressing, only there to be decorated by designers who can’t be bothered to read. Lorem Ipsum exists because words are powerful. If you fill up your page with draft copy about your client’s business, they will read it. They will comment on it. They will be inexorably drawn to it. Presented the wrong way, draft copy can send your design review off the rails.”</p>
  </section>

  <section class="process">
    <div class="process-photo" role="img" aria-label="Darkened group photo of the recruitment team standing together"></div>
    <h2 class="section-title">HOW WE WORK</h2>
    <div class="title-rule"></div>
    <p class="process-intro">Lorem Ipsum is simply has been the industry's standard dummy text everdummy texto the printing.</p>

    <svg class="process-map" width="814" height="462" viewBox="0 0 814 462">
      <defs>
        <g id="diamond">
          <rect x="-22" y="-22" width="44" height="44" transform="rotate(45)" fill="none" stroke="#fff" stroke-width="1" stroke-dasharray="2 2"/>
        </g>
        <g id="arrow-right" fill="none" stroke="#1e7fc4" stroke-width="1.2">
          <line x1="0" y1="0" x2="44" y2="0" stroke-dasharray="2 1.5" stroke-width=".8"/>
          <path d="M36-7l7 7-7 7M42-7l7 7-7 7"/>
        </g>
      </defs>

      <!-- Row one -->
      <use href="#diamond" x="198" y="172"/>
      <use href="#diamond" x="406" y="172"/>
      <use href="#diamond" x="616" y="172"/>
      <use href="#arrow-right" x="282" y="172"/>
      <use href="#arrow-right" x="490" y="172"/>

      <!-- select job: pointer -->
      <g fill="none" stroke="#fff" stroke-width="1.2">
        <circle cx="195" cy="162" r="3"/>
        <path d="M194 168v10l-3-2M194 172h6a3 3 0 0 1 3 3v4l-3 4h-5l-3-4"/>
      </g>
      <!-- online form: monitor -->
      <g fill="none" stroke="#fff" stroke-width="1.2">
        <rect x="395" y="162" width="22" height="15"/>
        <path d="M402 181h8M406 177v4M399 166h3M399 170h3M399 174h3M404 166h9M404 170h9M404 174h9"/>
      </g>
      <!-- interview: table -->
      <g fill="none" stroke="#fff" stroke-width="1.2">
        <circle cx="606" cy="164" r="2.5"/>
        <circle cx="626" cy="164" r="2.5"/>
        <path d="M601 181v-10h5l3 4M631 181v-10h-5l-3 4M607 175h18M616 175v6"/>
      </g>

      <text class="step-label" x="198" y="222" text-anchor="middle">SELECT YOUR JOB</text>
      <text class="step-label" x="406" y="222" text-anchor="middle">FILLUP ONLINE FORM</text>
      <text class="step-label" x="616" y="222" text-anchor="middle">FACE OFF INTERVIEW</text>

      <!-- Brand box -->
      <rect x="309" y="250" width="197" height="47" fill="none" stroke="#1e7fc4" stroke-width="1.2"/>
      <text class="map-brand" x="407.5" y="279" text-anchor="middle">BRIGHTCREW</text>

      <!-- Down arrow -->
      <g fill="none" stroke="#1e7fc4" stroke-width="1.2">
        <line x1="616" y1="248" x2="616" y2="292" stroke-dasharray="2 1.5" stroke-width=".8"/>
        <path d="M609 284l7 7 7-7M609 290l7 7 7-7"/>
      </g>

      <!-- Row two -->
      <use href="#diamond" x="198" y="353"/>
      <use href="#diamond" x="406" y="353"/>
      <use href="#diamond" x="616" y="353"/>
      <use href="#arrow-right" transform="translate(330 353) scale(-1 1)"/>
      <use href="#arrow-right" transform="translate(539 353) scale(-1 1)"/>

      <!-- get job: briefcase -->
      <g fill="none" stroke="#fff" stroke-width="1.2">
        <rect x="188" y="346" width="20" height="14" rx="1"/>
        <path d="M194 346v-3h8v3M188 352h20"/>
      </g>
      <!-- email -->
      <g fill="none" stroke="#fff" stroke-width="1.2">
        <rect x="396" y="345" width="20" height="14"/>
        <path d="M396 345l10 8 10-8"/>
      </g>
      <!-- test: laptop -->
      <g fill="none" stroke="#fff" stroke-width="1.2">
        <rect x="607" y="344" width="18" height="12"/>
        <path d="M603 360h26M611 348h3M611 352h3M616 348h6M616 352h6"/>
      </g>

      <text class="step-label" x="198" y="402" text-anchor="middle">GET THE JOB</text>
      <text class="step-label" x="406" y="402" text-anchor="middle">GET E-MAIL/CALL</text>
      <text class="step-label" x="616" y="402" text-anchor="middle">CRACK MACHINE TEST</text>
    </svg>
  </section>

</div>
</body>
</html>
```